Book Cover for Self Help Book Teens

I need a standard a5 size book cover (front and back) for my new self help book for teens. The book is called
WHEN DAYS DRAG
ideas and tactics for teens in tough times
break ups, school problems, procrastination, fights, sexuality, alcohol, bitchiness, eating problems, can’t sleep, no motivation, not allowed to do stuff, being on the outer..and 34 other common situations that every day Australian teens face
Marisol Penhale
psychologist for teens
I would like a very sparse,very modern cover, no photos - maybe just cartoon-y graphic of smiley face upside down - ie frowny face. Few colours in order to make it look bold. lots of space on the cover.
I will provide back cover text soon
Updates
I just want to say that I really appreciate all of your efforts, the designs were excellent. As a thankyou, I'm happy to email you a link to the e-version of this book if you are interested. Just email me at marisolpenhale@brightwavemail.net and I will send it through as soon as it is completed.
Target Market(s)
teens....but parents will also be buying book
Industry/Entity Type
School
Look and feel

```html
<!DOCTYPE html>
<html lang="en">
<head>
<meta charset="utf-8">
<title>When Days Drag – Book Cover</title>
<link rel="stylesheet" href="https://fonts.googleapis.com/css2?family=Permanent+Marker&family=Comic+Neue:wght@400;700&display=swap">
<style>
  :root {
    --page-bg: #ececec;
    --cover-bg: #ffffff;
    --ink: #111111;
    --title-orange: #e8842a;
    --face-light: #fbc431;
    --face-dark: #e57f22;
    --link-orange: #e8742a;
    --isbn-bg: #111111;
    --isbn-text: #ffffff;
  }
  * { box-sizing: border-box; margin: 0; padding: 0; }
  html, body { width: 1200px; height: 900px; overflow: hidden; }
  body {
    background: var(--page-bg);
    display: flex;
    gap: 50px;
    justify-content: center;
    align-items: center;
    font-family: "Comic Neue", "Comic Sans MS", cursive;
    color: var(--ink);
  }
  .cover {
    position: relative;
    width: 520px;
    height: 740px;
    background: var(--cover-bg);
    box-shadow: 0 6px 24px rgba(0,0,0,.18);
  }

  /* Title: plain set type, one colour, one weight */
  .book-title {
    font-family: "Comic Neue", "Comic Sans MS", cursive;
    font-weight: 700;
    color: var(--title-orange);
    line-height: .9;
  }
  .book-title span { display: block; }
  .book-title .title-when { font-size: .3em; margin-bottom: .15em; }

  /* Front */
  .front-title { position: absolute; top: 80px; left: 60px; font-size: 104px; }
  .front-title span + span + span { margin-left: 40px; }
  .subtitle {
    position: absolute; top: 345px; left: 60px; width: 400px;
    font-family: "Permanent Marker", "Comic Neue", cursive; font-size: 25px; line-height: 1.15;
  }
  .face-graphic {
    position: absolute; top: 440px; left: 185px; width: 150px; height: 150px;
  }
  .author {
    position: absolute; bottom: 58px; left: 0; right: 0; text-align: center;
    font-family: "Permanent Marker", "Comic Neue", cursive; font-size: 30px; line-height: 1;
  }
  .author small { display: block; font-size: 13px; margin-top: 6px; margin-left: 100px; }

  /* Back */
  .back-text { position: absolute; top: 28px; left: 28px; right: 28px; font-size: 11.2px; line-height: 1.32; }
  .back-intro { width: 240px; }
  .back-title { position: absolute; top: 8px; right: 20px; font-size: 48px; }
  .topics-label { margin-top: 4px; }
  .topic { margin-top: 13px; }
  .topic b { text-transform: uppercase; }
  .website {
    position: absolute; bottom: 68px; left: 120px;
    color: var(--link-orange); font-size: 12px;
  }
  .isbn-box {
    position: absolute; bottom: 26px; right: 28px; width: 108px; height: 40px;
    background: var(--isbn-bg); color: var(--isbn-text);
    font-family: Georgia, "Times New Roman", serif; font-size: 30px;
    display: flex; align-items: center; justify-content: center; letter-spacing: 1px;
  }
</style>
</head>
<body>

  <section class="cover cover-back">
    <div class="back-text">
      <p class="book-title back-title"><span class="title-when">WHEN</span><span>DAYS</span><span>DRAG</span></p>
      <p class="back-intro">Marisol Penhale is a clinical psychologist and has worked with hundreds of teens in the last 15 years. In this book she adresses 30 of the most frequent stressful and scary issues that teens face, and gives extremely practical what to do (and what NOT to do) advice in each situation.</p>
      <p class="topics-label">Topics include:</p>
      <p><b>FRIENDSHIPS:</b> My other friends seem to like each other more than me.....My friends are bitching about a friend of mine.....People at my school are horrible to me.....I have hardly any friends.....My friend is really depressed and I don't know what to do.....</p>
      <p class="topic"><b>Relationships:</b> I hate being single.....I think I'm gay/bi : How do I know for sure?....My boyfriend/girlfriend broke up with me and I'm devastated.....I've sent my boyfriend naked pics of myself, is this really that bad?....I cheated on my boyfriend/girlfriend and I feel guilty.....My boyfriend/girlfriend cheated on me.....I don't feel good about having sex with this person...</p>
      <p class="topic"><b>Parents:</b> My parents are ALWAYS nagging me to do stuff I don't want to do.....My parents don't let me do anything or if I'm allowed it has to be this big drama......I've had a massive fight with my parents (again) and feel totally furious with them......My parents and I just don't have anything in common; we hardly ever talk......</p>
      <p class="topic"><b>School:</b> I've really got to do homework but I have zero motivation.....I really can't stand my school and want to move but my parents won't let me.....I'm seriously behind, have way too much to do and I'm not going to get it all done.....This assignment/work at school/course is just too complicated, I'm not smart enough......</p>
      <p class="topic"><b>Health and self:</b> My sleep is terrible.....I drank way too much last night and probably last weekend as well.....I need to stop smoking weed/taking pills ......I hate the way I look.......I'm skipping meals; I feel guilty but I need to lose weight.....I cut myself and it makes me feel better......I think about awful things - I could never tell anyone about them......Sometimes I feel so angry, I feel out of control.......I</p>
    </div>
    <p class="website">www.growingheadsclinic.net</p>
    <div class="isbn-box">ISBN</div>
  </section>

  <section class="cover cover-front">
    <h1 class="book-title front-title"><span class="title-when">WHEN</span><span>DAYS</span><span>DRAG</span></h1>
    <p class="subtitle">Ideas and tactics for teens in tough times</p>
    <svg class="face-graphic" viewBox="0 0 150 150" role="img" aria-label="Cartoon upside-down smiley graphic">
      <defs>
        <radialGradient id="faceFill" cx="40%" cy="30%" r="75%">
          <stop offset="0" stop-color="#fbc431"/>
          <stop offset="1" stop-color="#e57f22"/>
        </radialGradient>
      </defs>
      <circle cx="75" cy="75" r="70" fill="url(#faceFill)"/>
    </svg>
    <p class="author">Marisol Penhale<small>Psychologist for teens</small></p>
  </section>

</body>
</html>
```